Website Design for Hulls for Heroes

Please design and code a new website.
Here are the sites I like best:
http://www.wavelorn.com/alternate/
http://www.wheelsforpatriots.org
Please make it similar. This is NOT a car donation site. It's a boat donation site. I just like this sites above as a lead generation sites.
Old site:
http://hullsforheroes.org
Updates
Coding
Coded - Design and coding required
Number of Pages Required
1 page
Look and feel

```html
<!DOCTYPE html>
<html lang="en">
<head>
<meta charset="utf-8">
<title>Hulls for Heroes – Donate Your Boat</title>
<link href="https://fonts.googleapis.com/css2?family=Open+Sans:wght@400;600;700;800&family=Roboto+Condensed:wght@700&display=swap" rel="stylesheet">
<style>
:root{
  --navy:#0b2a7a;
  --navy-deep:#071d58;
  --blue:#1f4aa8;
  --red:#a8201a;
  --red-bright:#c8261d;
  --ink:#1c1c1c;
  --grey:#555;
  --line:#d7d7d7;
  --white:#fff;
  --sage:#c9dcb8;
  --black:#0a0a0a;
}
*{margin:0;padding:0;box-sizing:border-box}
html,body{width:1200px;height:2786px;overflow:hidden}
body{position:relative;font-family:"Open Sans",Arial,sans-serif;color:var(--ink);background:var(--white)}
.abs{position:absolute}

/* header */
.site-header{left:0;top:0;width:1200px;height:158px;background:linear-gradient(100deg,#1a3c8c 0%,#2a55b0 55%,#16357f 100%)}
.brand{left:84px;top:50px;display:flex;align-items:center;gap:16px}
.brand-dot{width:46px;height:46px;border-radius:50%;background:var(--red-bright)}
.brand-name{font-family:"Roboto Condensed",sans-serif;font-weight:700;font-size:34px;color:var(--white);letter-spacing:.5px;text-transform:uppercase}
.call-box{left:790px;top:24px;display:flex;align-items:center;gap:16px;color:var(--white)}
.call-box .label{font-weight:800;font-size:21px;line-height:1}
.call-box .number{font-weight:800;font-size:38px;line-height:1.05}
.call-box .note{font-weight:700;font-size:13px;white-space:nowrap}

/* nav */
.main-nav{left:0;top:158px;width:1200px;height:42px;background:var(--black)}
.main-nav a{position:absolute;top:11px;color:var(--white);font-weight:700;font-size:16px;text-decoration:none}
.donate-tab{left:795px;top:150px;width:371px;height:58px;background:var(--red);color:var(--white);font-weight:700;font-size:19px;text-align:center;padding-top:22px}
.donate-tab svg{position:absolute;left:172px;top:-14px}

/* hero */
.hero{left:0;top:200px;width:1200px;height:496px;background:linear-gradient(180deg,#c9d8e6 0%,#e9eef2 55%,#dfe4e6 100%)}
.hero-photo{left:0;top:200px;width:795px;height:496px;background:radial-gradient(ellipse at 30% 55%,#b9a27e 0%,#8a8466 30%,transparent 60%),linear-gradient(180deg,#c6d6e4,#e7ebee)}
.donate-form{left:795px;top:208px;width:357px;height:488px;background:var(--navy);padding:28px 17px 0}
.form-title{color:var(--white);font-weight:700;font-size:15px;text-align:center;margin-bottom:16px}
.form-row{display:flex;gap:11px;margin-bottom:11px}
.field{flex:1;height:31px;background:var(--white);font-size:12px;font-weight:600;color:#223;padding:7px 6px;position:relative}
.field.select::after{content:"";position:absolute;right:9px;top:12px;border:6px solid transparent;border-top:8px solid #667}
.donate-btn{margin-top:12px;width:156px;height:41px;background:var(--red);color:var(--white);font-weight:700;font-size:15px;text-align:center;line-height:41px}

/* banner */
.banner{left:0;top:696px;width:1200px;height:199px;background:linear-gradient(90deg,#20242e,#3a2a2c 45%,#1d2340 100%)}
.banner-hex{left:0;top:696px}
.banner-copy{left:0;top:724px;width:520px;text-align:center;color:var(--white);font-weight:800}
.banner-copy .top{font-size:27px}
.banner-copy .big{font-family:"Roboto Condensed",sans-serif;font-size:62px;color:var(--sage);line-height:1.05}
.banner-copy .bottom{font-size:30px}
.perk{width:150px;text-align:center;color:var(--white);font-weight:700;font-size:14px;line-height:1.25}
.perk svg{display:block;margin:0 auto 10px}

/* section titles */
.section-title{width:1200px;text-align:center;font-weight:800;font-size:30px;color:var(--navy);display:flex;justify-content:center;align-items:center;gap:22px}
.section-title::before,.section-title::after{content:"";width:96px;height:1px;background:#9aa}
.section-title .accent{color:var(--red)}
.step h3{font-size:14.5px;font-weight:800;color:var(--navy);text-transform:uppercase;line-height:1.3;margin-bottom:12px}
.step p{font-size:14px;font-weight:600;color:#333;line-height:1.45}

/* why */
.why{left:0;top:1263px;width:1200px;height:414px;background:linear-gradient(180deg,#1d3b86,#102a6c)}
.why-title{color:var(--white)}
.why-title::before,.why-title::after{background:#c8d0e8}
.why-list{left:139px;top:1392px;list-style:none}
.why-list li{display:flex;align-items:center;gap:14px;height:33.5px;color:var(--white);font-size:14px}
.why-list b{font-weight:700}
.why-list svg{flex:none}

/* faq */
.faq-photo{left:80px;top:1798px;width:520px;height:425px;background:linear-gradient(135deg,#9a1f24 0%,#c7c7cf 35%,#1d3a7a 60%,#2a2f45 100%)}
.faq-item{left:633px;width:489px;border:1px solid var(--line);border-radius:6px;background:var(--white);padding:0 16px}
.faq-item .q{height:40px;display:flex;align-items:center;justify-content:space-between;font-weight:700;font-size:15px;color:#1f2f5a}
.faq-item .q svg{flex:none}
.faq-item .a{font-size:13.5px;color:#555;line-height:1.55;padding-bottom:12px}

/* footer */
.site-footer{left:0;top:2288px;width:1200px;height:455px;background:linear-gradient(90deg,#3a0f14 0%,#6a1a1e 30%,#14224d 70%,#0c1838 100%)}
.footer-brand{left:0;top:2350px;width:1200px;display:flex;justify-content:center;align-items:center;gap:16px}
.footer-col{color:var(--white)}
.footer-col h4{font-size:15px;font-weight:700;text-transform:uppercase;margin-bottom:30px}
.footer-col p,.footer-col li{font-size:12.5px;font-weight:700;line-height:1.4;list-style:none}
.badge{width:150px;height:42px;border-radius:4px;background:#e9edf3;margin-bottom:12px}
.badge.round{width:50px;height:50px;border-radius:50%}
.footer-call{left:780px;top:2460px;width:349px;height:145px;border:2px solid var(--white);border-radius:8px;background:var(--navy);padding:0 0 0 20px;display:flex;align-items:center}
.footer-call .call-box{position:static;gap:12px}
.footer-call .label{font-size:17px}
.footer-call .number{font-size:29px}
.footer-call .note{font-size:11px}
.copyright{left:0;top:2743px;width:1200px;height:43px;background:var(--white);text-align:center;font-size:12.5px;font-weight:700;color:#222;line-height:43px}
</style>
</head>
<body>

<header class="site-header abs">
  <div class="brand abs"><span class="brand-dot"></span><span class="brand-name">Hulls for Heroes</span></div>
  <div class="call-box abs">
    <svg width="76" height="76" viewBox="0 0 76 76"><circle cx="38" cy="38" r="35" fill="none" stroke="#fff" stroke-width="3"/><path d="M27 20c2-1 4 0 5 2l3 6c1 2 0 4-1 5l-3 2c2 5 6 9 11 11l2-3c1-1 3-2 5-1l6 3c2 1 3 3 2 5l-2 4c-1 2-3 3-6 3-14-1-26-13-27-27 0-3 1-5 3-6z" fill="#fff"/></svg>
    <div><div class="label">CALL TODAY TO DONATE</div><div class="number">1-800-555-0142</div><div class="note">Live Operators Available - 7 Days A Week</div></div>
  </div>
</header>

<nav class="main-nav abs">
  <a href="#how" style="left:176px">HOW TO DONATE</a>
  <a href="#why" style="left:364px">WHY DONATE</a>
  <a href="#faq" style="left:525px">FAQ</a>
  <a href="#about" style="left:609px">ABOUT</a>
</nav>

<section class="hero abs"></section>
<div class="hero-photo abs" role="img" aria-label="Soldier in camouflage hugging a child, a white motor yacht and a sketched city skyline behind"></div>
<div class="donate-tab abs">
  <svg width="28" height="28" viewBox="0 0 28 28"><circle cx="14" cy="14" r="13" fill="#a8201a" stroke="#fff" stroke-width="2"/><path d="M6 16h16l-3 5H9z M11 10h6v5h-6z" fill="#fff"/></svg>
  DONATE YOUR BOATS ONLINE
</div>
<form class="donate-form abs">
  <div class="form-title">Full Tax Deduction - Running or Not</div>
  <div class="form-row"><div class="field">First Name</div><div class="field">Last Name</div></div>
  <div class="form-row"><div class="field">Daytime Phone</div><div class="field">Email</div></div>
  <div class="form-row"><div class="field">Pickup Address</div></div>
  <div class="form-row"><div class="field">Pickup City</div></div>
  <div class="form-row"><div class="field select">Pickup State</div><div class="field">Zip Code</div></div>
  <div class="form-row"><div class="field select">Choose Year</div><div class="field select">Choose Make</div></div>
  <div class="form-row"><div class="field">Vehicle Model</div></div>
  <div class="donate-btn">DONATE NOW</div>
</form>

<section class="banner abs" role="img" aria-label="Dark background of waving flags"></section>
<svg class="banner-hex abs" width="560" height="199" viewBox="0 0 560 199"><polygon points="0,0 500,0 540,100 500,199 0,199" fill="#a8201a"/><polygon points="500,0 560,0 540,100" fill="#0b2a7a"/><polygon points="500,199 560,199 540,100" fill="#0b2a7a"/></svg>
<div class="banner-copy abs"><div class="top">DONATE YOUR BOATS TO</div><div class="big">VETERANS</div><div class="bottom">MAKE A DIFFERENCE</div></div>

<div class="perk abs" style="left:553px;top:730px">
  <svg width="60" height="60" viewBox="0 0 60 60"><circle cx="30" cy="30" r="26" fill="none" stroke="#fff" stroke-width="4"/><path d="M18 30l9 9 18-20" fill="none" stroke="#fff" stroke-width="5"/></svg>You have<br>no costs</div>
<div class="perk abs" style="left:705px;top:730px">
  <svg width="60" height="60" viewBox="0 0 60 60"><path d="M6 36h48l-8 10H14z M20 24h18l4 10H18z" fill="#fff"/></svg>Free pickup,<br>running or not</div>
<div class="perk abs" style="left:859px;top:730px">
  <svg width="60" height="60" viewBox="0 0 60 60"><rect x="14" y="6" width="32" height="48" fill="none" stroke="#fff" stroke-width="3"/><path d="M20 36h20M20 42h20M20 48h20" stroke="#fff" stroke-width="2"/><text x="30" y="28" fill="#fff" font-size="16" font-weight="700" text-anchor="middle" font-family="Open Sans,sans-serif">$</text></svg>We issue you an<br>IRS tax receipt</div>
<div class="perk abs" style="left:1008px;top:730px">
  <svg width="60" height="60" viewBox="0 0 60 60"><rect x="20" y="8" width="28" height="40" fill="none" stroke="#fff" stroke-width="3"/><path d="M26 18h16M26 25h16M26 32h16" stroke="#fff" stroke-width="2"/><circle cx="18" cy="38" r="8" fill="none" stroke="#fff" stroke-width="3"/><path d="M12 44l-6 8" stroke="#fff" stroke-width="4"/></svg>We take care of<br>all paperwork.</div>

<h2 id="how" class="section-title abs" style="left:0;top:975px"><span>HOW TO <span class="accent">DONATE</span></span></h2>

<div class="step abs" style="left:80px;top:1053px">
  <svg width="70" height="100" viewBox="0 0 70 100"><rect x="0" y="0" width="70" height="12" fill="#0b2a7a"/><rect x="0" y="20" width="12" height="12" fill="#0b2a7a"/><rect x="18" y="20" width="52" height="12" fill="#0b2a7a"/><rect x="0" y="40" width="70" height="12" fill="#0b2a7a"/><circle cx="16" cy="70" r="10" fill="#0b2a7a"/><path d="M10 78l-6 20 12-8 6 8-2-20" fill="#0b2a7a"/></svg>
</div>
<div class="step abs" style="left:162px;top:1092px;width:250px"><h3>Call us at 1-800-555-0142 or fill out the online form</h3><p>Donating your boat is easy and donation is accepted nationwide.</p></div>

<div class="step abs" style="left:446px;top:1070px">
  <svg width="70" height="50" viewBox="0 0 70 50"><path d="M0 22h70l-12 24H10z" fill="#a8201a"/><rect x="22" y="4" width="28" height="16" fill="#a8201a"/><rect x="28" y="8" width="6" height="6" fill="#fff"/><rect x="38" y="8" width="6" height="6" fill="#fff"/></svg>
</div>
<div class="step abs" style="left:553px;top:1092px;width:240px"><h3>We pick up the boat</h3><p>Any boats is accepted and we will arrange to pick up your boat when it is most convenient for you.</p></div>

<div class="step abs" style="left:845px;top:1048px">
  <svg width="75" height="75" viewBox="0 0 75 75"><rect x="10" y="4" width="46" height="62" fill="none" stroke="#0b2a7a" stroke-width="3"/><rect x="18" y="12" width="30" height="22" fill="none" stroke="#0b2a7a" stroke-width="2"/><text x="33" y="30" fill="#a8201a" font-size="18" font-weight="700" text-anchor="middle" font-family="Open Sans,sans-serif">$</text><path d="M18 42h30M18 50h30M18 58h30" stroke="#0b2a7a" stroke-width="3"/></svg>
</div>
<div class="step abs" style="left:942px;top:1092px;width:210px"><h3>Tax write-off</h3><p>Once the boat donation is complete, you will receive your tax deductable boat donation receipt.</p></div>

<section id="why" class="why abs" role="img" aria-label="Blue-tinted photograph of soldiers saluting before a flag"></section>
<h2 class="section-title why-title abs" style="left:0;top:1313px"><span>WHY DONATE YOUR BOATS TO US</span></h2>
<ul class="why-list abs">
  <li><svg width="24" height="24" viewBox="0 0 24 24"><circle cx="12" cy="12" r="11" fill="#c8261d"/><path d="M7 12h9M12 7l5 5-5 5" fill="none" stroke="#fff" stroke-width="2.2"/></svg><span><b>Harborline Trust Top Rated &amp; IRS 501(c)3 Approved :</b> Free 24/7 Pickup with No DMV Hassles.</span></li>
  <li><svg width="24" height="24" viewBox="0 0 24 24"><circle cx="12" cy="12" r="11" fill="#c8261d"/><path d="M7 12h9M12 7l5 5-5 5" fill="none" stroke="#fff" stroke-width="2.2"/></svg><span><b>Free Local Towing :</b> We will pick up your boat donation, running or not, when it's most convenient.</span></li>
  <li><svg width="24" height="24" viewBox="0 0 24 24"><circle cx="12" cy="12" r="11" fill="#c8261d"/><path d="M7 12h9M12 7l5 5-5 5" fill="none" stroke="#fff" stroke-width="2.2"/></svg><span><b>All Boats Accepted :</b> We take your car regardless of its condition or registration status.</span></li>
  <li><svg width="24" height="24" viewBox="0 0 24 24"><circle cx="12" cy="12" r="11" fill="#c8261d"/><path d="M7 12h9M12 7l5 5-5 5" fill="none" stroke="#fff" stroke-width="2.2"/></svg><span><b>Income Tax Deduction :</b> We issue you an IRS tax receipt &amp; offer the largest resale network to get you the highest tax write-off possible.</span></li>
  <li><svg width="24" height="24" viewBox="0 0 24 24"><circle cx="12" cy="12" r="11" fill="#c8261d"/><path d="M7 12h9M12 7l5 5-5 5" fill="none" stroke="#fff" stroke-width="2.2"/></svg><span><b>No Paperwork Hassles :</b> We take any boat and handle everything: DMV, Smog and IRS paperwork.</span></li>
  <li><svg width="24" height="24" viewBox="0 0 24 24"><circle cx="12" cy="12" r="11" fill="#c8261d"/><path d="M7 12h9M12 7l5 5-5 5" fill="none" stroke="#fff" stroke-width="2.2"/></svg><span><b>Boat donations help fund programs :</b> And benefit Harbor Veterans Relief Fund. An IRS 501(c)3 nonprofit organization.</span></li>
  <li><svg width="24" height="24" viewBox="0 0 24 24"><circle cx="12" cy="12" r="11" fill="#c8261d"/><path d="M7 12h9M12 7l5 5-5 5" fill="none" stroke="#fff" stroke-width="2.2"/></svg><span><b>Schedule a Free Pickup :</b> Complete the form and a representative will call you to arrange a convenient time to pickup your boat.</span></li>
</ul>

<h2 id="faq" class="section-title abs" style="left:0;top:1729px"><span>FREQUENTLY ASKED <span class="accent">QUESTIONS</span></span></h2>
<div class="faq-photo abs" role="img" aria-label="Uniformed service member seen from behind, saluting the flag"></div>

<div class="faq-item abs" style="top:1805px"><div class="q">What types of boats can be donated?<svg width="14" height="14" viewBox="0 0 14 14"><path d="M3 5l4 4 4-4" fill="none" stroke="#333" stroke-width="2"/></svg></div></div>
<div class="faq-item abs" style="top:1853px"><div class="q">What paperwork do I need to donate my boat?<svg width="14" height="14" viewBox="0 0 14 14"><path d="M3 9l4-4 4 4" fill="none" stroke="#333" stroke-width="2"/></svg></div><div class="a">All you need is a title, free of all liens. We will request some general information from you at the time of donation such as, the year, make, and model of the boat, as well as its general mechanical condition. We accept all boats, running or non-running.</div></div>
<div class="faq-item abs" style="top:2005px"><div class="q">Is my donated boat tax -deductible?<svg width="14" height="14" viewBox="0 0 14 14"><path d="M3 5l4 4 4-4" fill="none" stroke="#333" stroke-width="2"/></svg></div></div>
<div class="faq-item abs" style="top:2053px"><div class="q">What if the boat is not registered in my name?<svg width="14" height="14" viewBox="0 0 14 14"><path d="M3 5l4 4 4-4" fill="none" stroke="#333" stroke-width="2"/></svg></div></div>
<div class="faq-item abs" style="top:2101px"><div class="q">How much will I receive as a tax deduction for my boat?<svg width="14" height="14" viewBox="0 0 14 14"><path d="M3 5l4 4 4-4" fill="none" stroke="#333" stroke-width="2"/></svg></div></div>
<div class="faq-item abs" style="top:2149px"><div class="q">When will I receive my tax receipt?<svg width="14" height="14" viewBox="0 0 14 14"><path d="M3 5l4 4 4-4" fill="none" stroke="#333" stroke-width="2"/></svg></div></div>
<div class="faq-item abs" style="top:2197px"><div class="q">How do I schedule a pick up?<svg width="14" height="14" viewBox="0 0 14 14"><path d="M3 5l4 4 4-4" fill="none" stroke="#333" stroke-width="2"/></svg></div></div>

<footer id="about" class="site-footer abs" role="img" aria-label="Dark red and blue flag backdrop"></footer>
<div class="footer-brand abs"><span class="brand-dot"></span><span class="brand-name">Hulls for Heroes</span></div>

<div class="footer-col abs" style="left:74px;top:2460px;width:270px">
  <h4>About Hulls for Heroes</h4>
  <p>Lorem ipsum dolor sit amet, consectetuer adipiscing elit, sed diam nonummy nibheu ismod tincidunt ut laoreet dolore magna aliquam erat volutpat. Ut wisi enim ad mini veniam, quis nostrud exerci tation ullamcor per suscipit lobortis nisl ut aliquip ex ea co modo consequat.</p>
</div>
<div class="footer-col abs" style="left:381px;top:2460px">
  <h4>Navigation</h4>
  <ul><li>HOW TO DONATE</li><li>WHY DONATE</li><li>FAQ</li><li>ABOUT</li></ul>
</div>
<div class="footer-col abs" style="left:555px;top:2460px">
  <h4>Safe &amp; Secure</h4>
  <div class="badge"></div>
  <div class="badge"></div>
  <div class="badge round"></div>
</div>
<div class="footer-call abs">
  <div class="call-box">
    <svg width="64" height="64" viewBox="0 0 76 76"><circle cx="38" cy="38" r="35" fill="none" stroke="#fff" stroke-width="3"/><path d="M27 20c2-1 4 0 5 2l3 6c1 2 0 4-1 5l-3 2c2 5 6 9 11 11l2-3c1-1 3-2 5-1l6 3c2 1 3 3 2 5l-2 4c-1 2-3 3-6 3-14-1-26-13-27-27 0-3 1-5 3-6z" fill="#fff"/></svg>
    <div><div class="label">CALL TODAY TO DONATE</div><div class="number">1-800-555-0142</div><div class="note">Live Operators Available - 7 Days A Week</div></div>
  </div>
</div>

<div class="copyright abs">COPYRIGHT © 2017 HULLS FOR HEROES. PRIVACY POLICY | TERMS &amp; CONDITIONS. ALL RIGHTS RESERVED.</div>

</body>
</html>
```